Shopfront Graphics , front,side doors, small wall and mall entry.

New graphics retail store opening.

We are looking for a contemporary store front graphic that screams, Graphics, colour and ATTENTION.

The Fascia is approximately 3m high x 5 metres wide. We envisage a lightbox along the top and graphics continuing across the glass below.

We then have the side wall and graphics approximately 2.5m x 10m, and then second floor with glass and concrete.

Can we try a theme that partially covers all walls ..window frames and glass...Not overdone, but similar to the area covered in my demo pic of another store...Not just limited to the paint splash...your ideas...concepts?
Updates

Just to save all graphicos time at the initial concept stage,

Can we just stick to the front signage and the successful designer can just continue theme on other windows..
ORRRRRR..if you really want to impress and you have time....as before do the lot!
Just looking for the THEME layout at first.

Thanks
DL

Please see new front windows...do not follow this designers image, please ignore. But please note the front door now on Right hand side of front. 

We do have an interesting angle now, I would like minimal graphics now. ZenoPrints on light box above glass...but do need some theme.

I will place on here some more printed samples from our logo.

Note we need the TV screens to be seen  but some nice pattern/design to hold all the windows together!!

Thanks Desmond

OK we seem to be going the wrong way with splashes now..Too much and starting to look TOO colourful and TOO messy...I have attached some images that I took off Pixelbarn that are more in keeping with what I am looking for. I will also send you a rough sketch of an interior plan or "LOOK". 

The inside of the store is being professionally designed..White on white.. I am thinking of introducing one vibrant stripe.
Hope this helps with the "FEEL".....

Target Market(s)

This shop is a high street location with a lot of pedestrians.
The store is being designed as a fun collaborative store with seating and computer stations where anyone can come in and design, Photobooks, full colour T shirts, posters, Photogifts such as Mugs, Mouse mats, Canvas fine art pictures....

General atmosphere is FUN, entertaing and based on consumers wandering in, a bit like the MAPLE HALL experience.

We also make commercial signage, vehicle wraps, acrylic signs, photocopy and print banners. Regular signshop products.

Industry/Entity Type

Retail

Font styles to use
Sans Serif

Colors
9bcb3b
e34197
33a6d7

Requirements
Must have
• Our logo.
Lets concentrate on the main front window and light box with logo....see new updated files.
ZenoPrints, as designed by artflock guys!!
Nice to have
• THe walls and windows should have a theme pattern, like the attached sign shop. I like that look with the full colour splash but we are very open to your ideas.
Should not have
• Pictures of CATS!

```html
<!DOCTYPE html>
<html lang="en">
<head>
<meta charset="utf-8">
<title>ZenoPrints – Shopfront Graphics</title>
<link rel="stylesheet" href="https://fonts.googleapis.com/css2?family=Open+Sans:wght@600;700&display=swap">
<style>
  :root {
    --backdrop: #5b5b5b;
    --frame: #ffffff;
    --pane: #5a5a5a;
    --sky-light: #f4fdff;
    --sky-edge: #cdf1fb;
    --ink: #2f2f2f;
    --lime: #9bcb3b;
    --magenta: #e34197;
    --cyan: #33a6d7;
    --violet: #c447e0;
    --sun: #f3d23a;
    --label-outline: #1e1e1e;
  }
  * { box-sizing: border-box; margin: 0; padding: 0; }
  html, body { width: 1200px; height: 1000px; overflow: hidden; }
  body { background: var(--backdrop); font-family: "Open Sans", Arial, sans-serif; }

  .shopfront { position: absolute; left: 112px; top: 38px; width: 976px; height: 924px; }

  .lightbox {
    position: absolute; left: 0; top: 0; width: 976px; height: 327px;
    background: radial-gradient(ellipse at 45% 40%, var(--sky-light) 0%, #e9fbff 55%, var(--sky-edge) 100%);
    display: flex; align-items: center; justify-content: center; gap: 22px;
  }
  .brand-mark { width: 34px; height: 34px; background: var(--magenta); margin-top: 40px; }
  .brand-name {
    font-weight: 700; font-size: 104px; color: var(--ink);
    letter-spacing: -2px; margin-top: 40px;
  }

  .divider { position: absolute; left: 0; top: 327px; width: 976px; height: 10px; background: var(--frame); border-top: 2px solid #cfcfcf; }

  .glazing { position: absolute; left: 0; top: 337px; width: 976px; height: 587px; background: var(--frame); }
  .pane { position: absolute; background: var(--pane); }
  .pane.c1 { left: 14px; width: 215px; }
  .pane.c2 { left: 243px; width: 215px; }
  .pane.c3 { left: 471px; width: 215px; }
  .pane.c4 { left: 699px; width: 184px; }
  .pane.transom { top: 10px; height: 87px; }
  .pane.lower { top: 106px; height: 467px; }

  .colour-band {
    position: absolute; left: 0; top: 670px; width: 883px; height: 240px;
    background: linear-gradient(90deg, var(--violet) 0%, var(--cyan) 25%, var(--magenta) 50%, var(--sun) 78%, var(--lime) 100%);
    opacity: 0.55;
  }

  .services { position: absolute; list-style: none; transform: rotate(-9deg); transform-origin: left top; }
  .services.left { left: 244px; top: 518px; }
  .services.right { left: 472px; top: 508px; }
  .services li {
    display: flex; align-items: center; gap: 2px;
    font-weight: 600; font-size: 29px; line-height: 44px; color: #fff; white-space: nowrap;
    text-shadow: -1.5px -1.5px 0 var(--label-outline), 1.5px -1.5px 0 var(--label-outline),
                 -1.5px 1.5px 0 var(--label-outline), 1.5px 1.5px 0 var(--label-outline);
  }
  .services svg { width: 18px; height: 30px; flex: none; }
</style>
</head>
<body>
  <main class="shopfront">
    <header class="lightbox">
      <span class="brand-mark"></span>
      <h1 class="brand-name">ZenoPrints</h1>
    </header>
    <div class="divider"></div>

    <section class="glazing">
      <div class="pane transom c1"></div>
      <div class="pane transom c2"></div>
      <div class="pane transom c3"></div>
      <div class="pane transom c4"></div>
      <div class="pane lower c1"></div>
      <div class="pane lower c2"></div>
      <div class="pane lower c3"></div>
      <div class="pane lower c4"></div>
    </section>

    <div class="colour-band" role="img" aria-label="Illustration area: colourful paint splash ribbon running across the lower windows"></div>

    <ul class="services left">
      <li><svg viewBox="0 0 18 30"><polyline points="14,4 4,15 14,26" fill="none" stroke="var(--magenta)" stroke-width="3"/></svg>Photo Books</li>
      <li><svg viewBox="0 0 18 30"><polyline points="14,4 4,15 14,26" fill="none" stroke="var(--cyan)" stroke-width="3"/></svg>T Shirts</li>
      <li><svg viewBox="0 0 18 30"><polyline points="14,4 4,15 14,26" fill="none" stroke="var(--lime)" stroke-width="3"/></svg>Photo Gifts</li>
    </ul>
    <ul class="services right">
      <li><svg viewBox="0 0 18 30"><polyline points="14,4 4,15 14,26" fill="none" stroke="var(--magenta)" stroke-width="3"/></svg>Banners</li>
      <li><svg viewBox="0 0 18 30"><polyline points="14,4 4,15 14,26" fill="none" stroke="var(--cyan)" stroke-width="3"/></svg>Shop Signage</li>
      <li><svg viewBox="0 0 18 30"><polyline points="14,4 4,15 14,26" fill="none" stroke="var(--lime)" stroke-width="3"/></svg>Printing</li>
    </ul>
  </main>
</body>
</html>
```